Design a Website Mockup for VELT

I need website mockups created in the form of PSD's for my website, VELT. VELT is a backend and editor for html websites. I have attached mockups sketched out on paper. I would like a very minimal, flat, and colourful design. Please note: there are multiple pages, but they are identical except for the editor box. Please do the same proportion on the psds as in the mockup .I have attached only one page and will attach the rest in the near future.

```html
<!DOCTYPE html>
<html lang="en">
<head>
<meta charset="utf-8">
<title>VELT – Editor</title>
<link rel="stylesheet" href="https://fonts.googleapis.com/css2?family=Quicksand:wght@500;700&family=Alegreya:ital,wght@0,400;1,400&family=Arimo:ital,wght@0,400;0,700;1,400&display=swap">
<style>
:root{
  --navy:#0f1a3c;
  --navy-warm:#3a1f3e;
  --cyan:#1fd6d0;
  --red:#e0202a;
  --paper:#ffffff;
  --panel:#f7fbfa;
  --ink:#111111;
  --rule:#d8d8d8;
}
*{box-sizing:border-box;margin:0;padding:0}
html,body{width:1200px;height:868px;overflow:hidden}
body{position:relative;background:var(--navy);font-family:"Quicksand",sans-serif}
.header-band{position:absolute;left:0;top:0;width:1200px;height:260px;
  background:linear-gradient(180deg,var(--navy-warm) 0%,var(--navy) 100%)}
.logo{position:absolute;left:28px;top:14px;font-size:108px;font-weight:700;letter-spacing:2px;line-height:1;color:var(--cyan)}
.menu{position:absolute;left:1068px;top:6px;color:var(--cyan);font-size:36px;font-weight:700;letter-spacing:1px;border-bottom:3px solid var(--cyan);line-height:1.05}
.side-link{position:absolute;color:var(--cyan);font-size:26px;font-weight:700;letter-spacing:1px;transform:rotate(-62deg);transform-origin:left bottom;white-space:nowrap}
.side-link.settings{left:1068px;top:160px}
.side-link.visual{left:1140px;top:128px}

.editor{position:absolute;left:33px;top:213px;width:644px;height:624px;background:var(--paper);overflow:hidden;font-family:"Arimo",sans-serif;color:var(--ink)}
.editor .topbar{position:absolute;left:0;top:10px;width:634px;height:5px;background:var(--ink)}
.editor .scrollbar{position:absolute;right:0;top:0;width:10px;height:100%;background:#eee;border-left:1px solid var(--rule)}
.editor .scrollbar::after{content:"";position:absolute;left:2px;top:14px;width:6px;height:230px;background:#c7c7c7}
.site-kicker{position:absolute;left:18px;top:24px;font-size:15px}
.site-title{position:absolute;left:16px;top:40px;font-size:40px;font-weight:700;white-space:nowrap;letter-spacing:-.5px}
.site-title small{font-size:18px;font-weight:400;letter-spacing:0}
.languages{position:absolute;left:22px;top:112px;width:600px;height:76px;background:linear-gradient(90deg,#d9dde6,#eee3e3,#dde6dd,#e6e0d6)}
.hero h1{position:absolute;left:0;top:198px;width:634px;text-align:center;font-family:"Alegreya",serif;font-size:60px;font-weight:400}
.hero .quote{position:absolute;left:0;top:283px;width:634px;text-align:center;font-style:italic;font-size:12.5px;line-height:1.2}
.hero .quote small{font-size:11px;display:block}
.cursor{position:absolute;left:118px;top:248px}
.col{position:absolute;top:325px;font-size:11.2px;line-height:1.33;text-align:justify}
.col.left{left:12px;width:320px}
.col.right{left:350px;width:272px}
.col h2{font-family:"Alegreya",serif;font-style:italic;font-weight:400;font-size:19px;line-height:1.2;margin:0 0 4px}
.col p{margin-bottom:12px}

.picker{position:absolute;left:747px;top:213px;width:380px;height:394px;background:var(--panel)}
.hex{position:absolute;left:148px;top:22px;font-size:19px;font-weight:700;color:var(--ink);display:flex;align-items:center;gap:6px}
.hex .field{width:68px;height:22px;border:1px solid #aaa;background:#fff;font-family:"Arimo",sans-serif;font-size:13px;font-weight:400;padding:2px 4px}
.hex .add{color:var(--cyan);font-size:30px;margin-left:16px;line-height:1}
.wheel{position:absolute;left:63px;top:75px;width:294px;height:294px;border-radius:50%;
  background:radial-gradient(circle,#fff 0,rgba(255,255,255,0) 70%),conic-gradient(from 0deg,#ff2a2a,#ffd21f 60deg,#6cf03a 120deg,#1fd6c8 180deg,#2b3cff 240deg,#e22be0 300deg,#ff2a2a)}
.wheel::after{content:"";position:absolute;left:141px;top:141px;width:10px;height:10px;border:1.5px solid #333;border-radius:50%}
.history{position:absolute;left:880px;top:627px}
.actions{position:absolute;left:733px;top:710px}
</style>
</head>
<body>
<div class="header-band" role="img" aria-label="Decorative header backdrop"></div>

<header>
  <div class="logo">VELT</div>
  <nav>
    <div class="menu">MENU</div>
    <div class="side-link settings">SETTINGS</div>
    <div class="side-link visual">VISUAL</div>
  </nav>
</header>

<main>
  <section class="editor" aria-label="Page editor">
    <div class="topbar"></div>
    <div class="site-kicker">Graphic designer,</div>
    <div class="site-title">Design Exceptional Websites <small>Code</small></div>
    <div class="languages" role="img" aria-label="Row of language selector links with country flags"></div>
    <div class="hero">
      <h1>Lorem Ipsum</h1>
      <div class="quote">"Neque porro quisquam est qui dolorem ipsum quia dolor sit amet, consectetur, adipisci velit..."<small>"There is no one who loves pain itself, who seeks after it and wants to have it, simply because it is pain..."</small></div>
    </div>
    <svg class="cursor" width="22" height="32" viewBox="0 0 22 32"><path d="M1 1v26l6-6 5 10 4-2-5-10h9z" fill="#111" stroke="#fff" stroke-width="1"/></svg>
    <div class="col left">
      <h2>What is Lorem Ipsum?</h2>
      <p><b>Lorem Ipsum</b> is simply dummy text of the printing and typesetting industry. Lorem Ipsum has been the industry's standard dummy text ever since the 1500s, when an unknown printer took a galley of type and scrambled it to make a type specimen book. It has survived not only five centuries, but also the leap into electronic typesetting, remaining essentially unchanged.</p>
      <h2>Where does it come from?</h2>
      <p>Contrary to popular belief, Lorem Ipsum is not simply random text. It has roots in a piece of classical Latin literature from 45 BC, making it over 2000 years old. Alder Finch, a Latin professor at Marlow Hill College in Virginia, looked up one of the more obscure Latin words, consectetur, and discovered the undoubtable source.</p>
    </div>
    <div class="col right">
      <h2>Why do we use it?</h2>
      <p>It is a long established fact that a reader will be distracted by the readable content of a page when looking at its layout. The point of using Lorem Ipsum is that it has a more-or-less normal distribution of letters, as opposed to using 'Content here, content here', making it look like readable English.</p>
      <h2>Where can I get some?</h2>
      <p>There are many variations of passages of Lorem Ipsum available, but the majority have suffered alteration in some form, by injected humour, or randomised words which don't look even slightly believable. All the generators on the Internet tend to repeat predefined chunks as necessary.</p>
    </div>
    <div class="scrollbar"></div>
  </section>

  <aside class="picker" aria-label="Colour picker">
    <div class="hex">HEX: <span class="field">FFFFFF</span><span class="add">+</span></div>
    <div class="wheel"></div>
  </aside>

  <svg class="history" width="150" height="44" viewBox="0 0 150 44" aria-label="Undo, save, redo">
    <g fill="none" stroke="var(--cyan)" stroke-width="4">
      <path d="M12 8h22v30H8"/><path d="M14 2l-8 6 8 6"/>
      <path d="M138 8h-22v30h26"/><path d="M136 2l8 6-8 6"/>
    </g>
    <rect x="58" y="6" width="32" height="32" fill="none" stroke="var(--red)" stroke-width="4"/>
    <rect x="66" y="6" width="16" height="12" fill="var(--red)"/>
  </svg>

  <svg class="actions" width="430" height="140" viewBox="0 0 430 140" aria-label="New page, publish, refresh">
    <g fill="none" stroke="var(--red)" stroke-width="11">
      <path d="M8 8h52l32 32v80H8z"/><path d="M58 8v34h34"/>
    </g>
    <g stroke="var(--cyan)" stroke-width="13"><path d="M80 68v68M46 102h68"/></g>
    <g fill="none" stroke="var(--red)" stroke-width="9">
      <circle cx="218" cy="62" r="50"/>
      <ellipse cx="218" cy="62" rx="22" ry="50"/>
      <path d="M168 62h100M176 36h84M176 88h84"/>
    </g>
    <path d="M226 66v70l16-16 14 20 12-8-14-20h22z" fill="var(--cyan)" stroke="var(--navy)" stroke-width="5"/>
    <path d="M398 84A54 54 0 1 1 386 28" fill="none" stroke="var(--red)" stroke-width="20"/>
    <path d="M358 8l56 0-10 54z" fill="var(--red)"/>
  </svg>
</main>
</body>
</html>
```